Veterinary Business cards

Redesign Business Card

Information needed on Card:
Hours: Mon-Fri: 4pm -10PM; Sat- Sun- 10 AM- 5PM
Help@tandrelyns.com
www.tandrelyns.com
405-718-2954
4170 SW 38th Ave. okc, ok 73119
*No appointment necessary*

Optional:
Our tag line is "We're here when you need us" - If it fits on the cards.

```html
<!DOCTYPE html>
<html lang="en">
<head>
<meta charset="utf-8">
<title>Tandrelyn's Urgent Care – Business Card</title>
<link href="https://fonts.googleapis.com/css2?family=Baloo+2:wght@400;700&family=Marcellus&display=swap" rel="stylesheet">
<style>
  :root {
    --backdrop: #ababab;
    --navy: #173b66;
    --orange: #d4791d;
    --cream: #f0ebe3;
    --white: #ffffff;
    --taupe: #8f8a84;
  }
  * { margin: 0; padding: 0; box-sizing: border-box; }
  html, body { width: 1200px; height: 1000px; overflow: hidden; }
  body { background: var(--backdrop); position: relative; font-family: "Baloo 2", sans-serif; }

  .card {
    position: absolute; left: 294px; width: 613px; height: 352px;
    border-radius: 24px; overflow: hidden;
    box-shadow: 0 18px 40px rgba(0,0,0,0.28);
  }
  .card--front { top: 125px; background: var(--navy); color: var(--white); }
  .card--back { top: 537px; background: var(--cream); }

  .contact {
    position: absolute; left: 20px; width: 322px; top: 0;
    text-align: center; line-height: 1.2;
  }
  .contact p { position: absolute; left: 0; width: 100%; }
  .hours { font-size: 18px; }
  .hours strong { font-weight: 700; }
  .hours--weekday { top: 48px; }
  .hours--weekend { top: 72px; }
  .phone { top: 118px; font-size: 19px; font-weight: 700; display: flex; justify-content: center; align-items: center; gap: 6px; }
  .phone svg { width: 17px; height: 17px; fill: var(--orange); }
  .web { top: 165px; font-size: 16px; font-weight: 700; }
  .email { top: 186px; font-size: 14px; }
  .address { top: 214px; font-size: 14px; line-height: 1.4; }
  .walk-in { top: 269px; font-size: 16px; font-weight: 700; }

  .corner-disc {
    position: absolute; left: 382px; top: 186px; width: 330px; height: 330px;
    border-radius: 50%; background: var(--orange);
  }
  .front-name {
    position: absolute; right: 32px; top: 296px;
    font-family: "Marcellus", serif; font-size: 22px; color: var(--cream);
    letter-spacing: 1px;
  }

  .skyline {
    position: absolute; left: 151px; top: 63px; width: 310px; height: 92px;
    background: linear-gradient(180deg, rgba(212,121,29,0.15), rgba(212,121,29,0.35));
    border-bottom: 2px solid var(--orange);
  }
  .back-name {
    position: absolute; left: 0; width: 100%; top: 158px; text-align: center;
    font-family: "Marcellus", serif; font-size: 40px; color: var(--navy);
    letter-spacing: 1px; line-height: 1;
  }
  .back-name span { display: block; font-size: 21px; letter-spacing: 3px; margin-top: 6px; }
  .tagline {
    position: absolute; left: 0; width: 100%; top: 250px; text-align: center;
    font-family: "Marcellus", serif; font-size: 24px; color: var(--taupe);
    line-height: 1.2;
  }
</style>
</head>
<body>
  <section class="card card--front">
    <div class="contact">
      <p class="hours hours--weekday"><strong>Mon-Fri:</strong> 4pm -10pm</p>
      <p class="hours hours--weekend"><strong>Sat- Sun:</strong> 10am- 5pm</p>
      <p class="phone">
        <svg viewBox="0 0 24 24" aria-hidden="true"><path d="M6.6 10.8c1.4 2.8 3.8 5.1 6.6 6.6l2.2-2.2c.3-.3.7-.4 1-.2 1.1.4 2.3.6 3.6.6.6 0 1 .4 1 1V20c0 .6-.4 1-1 1C10.6 21 3 13.4 3 4c0-.6.4-1 1-1h3.5c.6 0 1 .4 1 1 0 1.2.2 2.4.6 3.6.1.3 0 .7-.2 1L6.6 10.8z"/></svg>
        405-718-2954
      </p>
      <p class="web">www.tandrelyns.com</p>
      <p class="email">Help@tandrelyns.com</p>
      <p class="address">4170 SW 38th Ave.<br>okc, ok 73119</p>
      <p class="walk-in">*No Appointment Necessary*</p>
    </div>
    <div class="corner-disc"></div>
    <p class="front-name">TANDRELYN'S</p>
  </section>

  <section class="card card--back">
    <div class="skyline" role="img" aria-label="Outline illustration of a city skyline"></div>
    <p class="back-name">TANDRELYN'S<span>URGENT CARE</span></p>
    <p class="tagline">WE'RE HERE WHEN<br>YOU NEED US</p>
  </section>
</body>
</html>
```